PowerPoint Slide desk with a Rocketship theme

We are a company that is going through a lot of growth. We internally refer to it as being on a rocketship. Looking for a PowerPoint deck to use with my internal team. I would like it to be fun and cartoonish. The main theme is spaceships/rockets and going on a mission. We will be using this as a way to describe the mission of the company and what the goals of the company are. There should be a title page that can be reused for each team meeting held with a space for a title and date. There should be pages for lots of text. The text must be easy to read on a TV. There should be slides for photos and graphs.

I have included an image of a rocket and a space background. I have included another rocket for example of the type of drawing and look we are looking for. I have also included our company logo.

The rocketship should have the round Signal Forge logo on it. You can have fun and include some alien figures and spacemen.

Target Market(s)

This is for our internal employees. We are and IT company

Industry/Entity Type

Managed IT Services

Font styles to use
Sans Serif

Colors
0054AA
0677BA
7BADD7
CADEEF
E8F1F8

Requirements
Must have
• see images attached for examples of what we are looking for.

```html
<!DOCTYPE html>
<html lang="en">
<head>
<meta charset="utf-8">
<title>Signal Forge – Rocketship Slide Deck</title>
<link href="https://fonts.googleapis.com/css2?family=Poppins:wght@400;500;600;700;800&display=swap" rel="stylesheet">
<style>
:root{
  --page:#ffffff;
  --night:#0a1028;
  --night-2:#121a3a;
  --teal:#1bbfb2;
  --teal-2:#22d3c0;
  --blue-deep:#0054AA;
  --blue-mid:#0677BA;
  --sky:#7BADD7;
  --mist:#CADEEF;
  --ice:#E8F1F8;
  --violet:#5b47c9;
  --rose:#d9436f;
  --ink:#14203f;
  --muted:#5d6784;
  --white:#ffffff;
}
*{box-sizing:border-box;margin:0;padding:0}
html,body{width:1200px;height:2188px;overflow:hidden}
body{background:var(--page);font-family:"Poppins",sans-serif;color:var(--ink);position:relative}
.slide{position:absolute;width:440px;height:248px;overflow:hidden;background:var(--white);box-shadow:0 6px 18px rgba(10,30,70,.18)}
.col-left{left:150px}
.col-right{left:614px}
.dark{background:var(--night);color:var(--white)}
.brand{position:absolute;display:flex;align-items:center;gap:6px;font-size:10px;font-weight:700;color:var(--white);z-index:2}
.brand .dot{width:12px;height:12px;border-radius:50%;background:var(--white)}
.brand.on-light{color:var(--blue-deep)}
.brand.on-light .dot{background:var(--blue-deep)}
.pad{position:absolute;z-index:1}
.blob{position:absolute;border-radius:50%}
.label{font-size:9px;color:var(--teal);font-weight:600}
.title-xl{font-size:21px;font-weight:700;line-height:1.15}
.title-lg{font-size:18px;font-weight:700;line-height:1.15}
.accent{color:var(--teal)}
.accent-blue{color:var(--blue-deep)}
.body{font-size:8px;line-height:1.5;color:var(--muted)}
.body-light{font-size:8px;line-height:1.5;color:rgba(255,255,255,.85)}
.item-title{font-size:9px;font-weight:700}
.photo{position:absolute}
.grad-teal{background:linear-gradient(135deg,var(--teal-2),var(--blue-mid) 60%,var(--blue-deep))}
.grad-sky{background:linear-gradient(135deg,var(--sky),var(--violet))}
.btn{display:inline-block;font-size:8px;padding:3px 12px;border:1px solid var(--teal);color:var(--teal);border-radius:10px}
.stat b{display:block;font-size:12px;color:var(--blue-deep)}
.stat span{font-size:7px;color:var(--muted)}
.icon-circle{flex:none;width:18px;height:18px;border-radius:50%;background:var(--ice);border:1.5px solid var(--teal)}
.card{position:absolute;background:var(--white);border-radius:4px;box-shadow:0 3px 10px rgba(10,30,70,.15);padding:8px;z-index:1}
table{border-collapse:collapse;width:100%;font-size:8px}
td,th{padding:4px 5px;text-align:center}
th{color:var(--white);font-weight:600}
tbody tr{border-bottom:1px solid rgba(255,255,255,.14)}
tbody td{color:#d3dbef}
.page-no{position:absolute;right:10px;bottom:6px;font-size:7px;color:var(--muted)}
</style>
</head>
<body>

<!-- Left column -->
<section class="slide dark col-left" style="top:118px" aria-label="Title slide">
  <div class="blob" style="left:-60px;bottom:-90px;width:260px;height:160px;background:radial-gradient(circle,rgba(34,211,192,.55),rgba(34,211,192,0) 70%)"></div>
  <div class="blob" style="right:-40px;top:-60px;width:200px;height:150px;background:radial-gradient(circle,rgba(6,119,186,.6),rgba(6,119,186,0) 70%)"></div>
  <div class="brand" style="left:50%;top:22px;transform:translateX(-50%)"><span class="dot"></span>Signal Forge</div>
  <div class="pad" style="left:0;right:0;top:88px;text-align:center">
    <div class="label">Team Meeting</div>
    <div class="title-xl" style="margin-top:4px">Presentation Title Goes Here</div>
    <div style="font-size:8px;margin-top:8px;color:var(--teal)">John Doe <span style="color:var(--white)">|</span> 2021</div>
  </div>
</section>

<section class="slide col-left" style="top:390px" aria-label="Our beloved company">
  <div class="photo" role="img" aria-label="Astronaut floating in colourful neon light" style="left:22px;top:22px;width:150px;height:204px;background:linear-gradient(160deg,#0a0f28,#1d3a8a 40%,#7b3fa8 65%,#e0a04a 88%,#0a0f28)"></div>
  <div class="blob" style="right:-40px;top:-50px;width:120px;height:120px;background:var(--mist)"></div>
  <div class="brand on-light" style="right:18px;top:14px"><span class="dot"></span>Signal Forge</div>
  <div class="pad" style="left:194px;top:50px;width:226px">
    <div class="title-lg accent-blue">Our Beloved<br><span class="accent">Company</span></div>
    <p class="body" style="margin-top:8px">We grow fast and keep every client system running smoothly.</p>
    <div style="display:flex;gap:20px;margin-top:14px">
      <div class="stat"><b>+750</b><span>Clients</span></div>
      <div class="stat"><b>+650</b><span>Projects</span></div>
      <div class="stat"><b>+25</b><span>Years</span></div>
    </div>
  </div>
</section>

<section class="slide col-left" style="top:662px" aria-label="Our core value">
  <div class="blob grad-sky" style="left:-70px;bottom:-80px;width:180px;height:180px;opacity:.45"></div>
  <div class="brand on-light" style="right:18px;top:14px"><span class="dot"></span>Signal Forge</div>
  <div class="pad" style="left:24px;top:60px;width:160px">
    <div class="title-lg accent-blue">Our <span class="accent">Core Value</span></div>
    <p class="body" style="margin-top:6px">Values guide every mission we launch together.</p>
    <div style="margin-top:10px"><span class="btn">Read More</span></div>
  </div>
  <div class="pad" style="left:204px;top:46px;width:222px;display:grid;grid-template-columns:1fr 1fr;gap:14px 10px">
    <div style="display:flex;gap:5px"><div class="icon-circle"></div><div><p class="item-title">Teamwork</p><p class="body">Our crew lands every launch.</p></div></div>
    <div style="display:flex;gap:5px"><div class="icon-circle"></div><div><p class="item-title">Trust</p><p class="body">Clients rely on us daily.</p></div></div>
    <div style="display:flex;gap:5px"><div class="icon-circle"></div><div><p class="item-title">Growth</p><p class="body">We aim higher each orbit.</p></div></div>
    <div style="display:flex;gap:5px"><div class="icon-circle"></div><div><p class="item-title">Care</p><p class="body">Each system gets focus.</p></div></div>
  </div>
</section>

<section class="slide col-left" style="top:934px" aria-label="Leader company">
  <div class="blob grad-teal" style="right:-50px;bottom:-60px;width:150px;height:150px;opacity:.35"></div>
  <div class="brand on-light" style="right:18px;top:14px"><span class="dot"></span>Signal Forge</div>
  <div class="pad" style="left:0;right:0;top:26px;text-align:center">
    <div class="title-lg accent-blue">Leader <span class="accent">Company</span></div>
  </div>
  <div class="pad" style="left:44px;top:64px;display:flex;gap:16px">
    <div><div role="img" aria-label="Portrait of team leader" style="width:106px;height:116px;background:linear-gradient(160deg,var(--sky),var(--blue-deep))"></div><p class="item-title" style="margin-top:5px">Anna Lee</p><p class="body">CEO</p></div>
    <div><div role="img" aria-label="Portrait of team leader" style="width:106px;height:116px;background:linear-gradient(160deg,#c9b49c,#6b4a3a)"></div><p class="item-title" style="margin-top:5px">Mark Doyle</p><p class="body">CTO</p></div>
    <div><div role="img" aria-label="Portrait of team leader" style="width:106px;height:116px;background:linear-gradient(160deg,var(--mist),#3a4a6e)"></div><p class="item-title" style="margin-top:5px">Sara Quinn</p><p class="body">COO</p></div>
  </div>
</section>

<section class="slide col-left" style="top:1206px" aria-label="Our Signal Forge team">
  <div class="photo grad-teal" style="left:0;top:0;width:200px;height:248px"></div>
  <div class="photo" role="img" aria-label="Astronaut helmet close-up against space" style="left:200px;top:0;width:240px;height:248px;background:linear-gradient(150deg,#0a1638,#4a6a9a 45%,#b2562a 78%,#141a30)"></div>
  <div class="brand" style="left:22px;top:16px"><span class="dot"></span>Signal Forge</div>
  <div class="pad" style="left:22px;top:56px;width:166px;color:var(--white)">
    <div class="title-lg">Our Signal<br>Forge</div>
    <p class="body-light" style="margin-top:8px">Meet the crew that keeps us on course.</p>
    <div style="margin-top:14px;height:4px;width:130px;background:rgba(255,255,255,.3);border-radius:2px"><div style="height:4px;width:90px;background:var(--white);border-radius:2px"></div></div>
    <div style="margin-top:9px;height:4px;width:130px;background:rgba(255,255,255,.3);border-radius:2px"><div style="height:4px;width:64px;background:var(--white);border-radius:2px"></div></div>
  </div>
</section>

<section class="slide col-left" style="top:1478px" aria-label="Process infographic">
  <div class="photo grad-teal" style="left:0;top:0;width:440px;height:120px"></div>
  <div class="pad" style="left:0;right:0;top:20px;text-align:center;color:var(--white)"><div class="title-lg">Process Infographic</div></div>
  <div class="card" style="left:28px;top:62px;width:118px;height:154px">
    <p class="item-title" style="color:var(--blue-deep)">Plan</p><p class="body">Map out the mission.</p>
    <div role="img" aria-label="Cartoon satellite" style="margin:12px auto 0;width:62px;height:62px;border-radius:50%;background:linear-gradient(135deg,var(--ice),var(--sky))"></div>
  </div>
  <div class="card" style="left:161px;top:62px;width:118px;height:154px">
    <p class="item-title" style="color:var(--blue-deep)">Build</p><p class="body">Assemble the crew.</p>
    <div role="img" aria-label="Cartoon planet" style="margin:12px auto 0;width:62px;height:62px;border-radius:50%;background:linear-gradient(135deg,var(--sky),var(--blue-mid))"></div>
  </div>
  <div class="card" style="left:294px;top:62px;width:118px;height:154px">
    <p class="item-title" style="color:var(--blue-deep)">Launch</p><p class="body">Lift off together.</p>
    <div role="img" aria-label="Cartoon rocket lifting off" style="margin:12px auto 0;width:62px;height:62px;border-radius:50%;background:linear-gradient(135deg,#f2c14e,var(--rose) 50%,var(--violet))"></div>
  </div>
</section>

<section class="slide col-left" style="top:1750px;background:linear-gradient(135deg,var(--blue-deep),var(--blue-mid) 55%,var(--teal-2))" aria-label="Thank you">
  <div class="brand" style="left:50%;top:64px;transform:translateX(-50%);font-size:12px"><span class="dot"></span>Signal Forge</div>
  <div class="pad" style="left:0;right:0;top:96px;text-align:center;color:var(--white)">
    <div style="font-size:28px;font-weight:700">Thank You!</div>
    <p class="body-light" style="margin-top:6px">See you next mission</p>
  </div>
</section>

<!-- Right column -->
<section class="slide dark col-right" style="top:250px" aria-label="Title slide alternate">
  <div class="blob" style="right:-30px;top:-40px;width:130px;height:110px;background:var(--teal)"></div>
  <div class="blob" style="right:66px;top:12px;width:20px;height:20px;background:var(--teal-2)"></div>
  <div class="blob" style="right:20px;top:58px;width:11px;height:11px;background:var(--teal-2)"></div>
  <div class="blob" style="left:-70px;bottom:-100px;width:260px;height:170px;background:radial-gradient(circle,rgba(34,211,192,.4),rgba(34,211,192,0) 70%)"></div>
  <div class="brand" style="left:22px;top:18px"><span class="dot"></span>Signal Forge</div>
  <div class="pad" style="left:22px;top:92px">
    <div class="label">Team Meeting</div>
    <div class="title-xl" style="margin-top:4px">Presentation Title Goes Here</div>
    <div style="font-size:8px;margin-top:8px;color:var(--teal)">John Doe <span style="color:var(--white)">|</span> 2021</div>
  </div>
</section>

<section class="slide col-right" style="top:522px" aria-label="Company mission">
  <div class="photo" role="img" aria-label="Starry space backdrop" style="inset:0;background:linear-gradient(135deg,#0a1438,#0d3370 50%,#0a1430)"></div>
  <div class="brand" style="left:22px;top:16px"><span class="dot"></span>Signal Forge</div>
  <div class="pad" style="left:22px;top:56px;width:180px;color:var(--white)">
    <div class="title-lg">Company <span class="accent">Mission</span></div>
    <p style="font-size:18px;font-weight:700;margin-top:12px;line-height:.8;color:var(--teal)">“</p>
    <p class="body-light">Reach for the stars, land safely.</p>
  </div>
  <div class="pad" style="left:248px;top:36px;width:176px;color:var(--white);display:flex;flex-direction:column;gap:10px">
    <div style="border-left:2px solid var(--teal);padding-left:7px"><p class="item-title">Connect</p><p class="body-light">Link every team with care.</p></div>
    <div style="border-left:2px solid var(--teal);padding-left:7px"><p class="item-title">Protect</p><p class="body-light">Keep client data safe.</p></div>
    <div style="border-left:2px solid var(--teal);padding-left:7px"><p class="item-title">Support</p><p class="body-light">Answer fast, fix it right.</p></div>
    <div style="border-left:2px solid var(--teal);padding-left:7px"><p class="item-title">Grow</p><p class="body-light">Scale with each launch.</p></div>
  </div>
</section>

<section class="slide col-right" style="top:794px" aria-label="Our company space images">
  <div class="blob grad-sky" style="right:-40px;top:-40px;width:140px;height:140px;opacity:.45"></div>
  <div class="blob" style="right:8px;top:24px;width:56px;height:56px;background:var(--rose);opacity:.65"></div>
  <div class="photo" role="img" aria-label="Astronaut drifting in deep space" style="left:22px;top:22px;width:110px;height:204px;background:linear-gradient(170deg,#0a1a3a,var(--blue-mid) 60%,#0a1030)"></div>
  <div class="photo" role="img" aria-label="Colourful nebula" style="left:142px;top:22px;width:110px;height:204px;background:linear-gradient(170deg,#1b0f3a,#6a2a8a 45%,#d25a9a 72%,#130a26)"></div>
  <div class="pad" style="left:270px;top:78px;width:156px">
    <div class="title-lg accent-blue">Our Company <span class="accent">Spaceimages</span></div>
    <p class="body" style="margin-top:6px">Snapshots from our journey so far.</p>
  </div>
</section>

<section class="slide col-right" style="top:1066px;background:linear-gradient(135deg,var(--teal-2),var(--blue-mid) 55%,var(--blue-deep))" aria-label="Company spacegraph">
  <div class="pad" style="left:0;right:0;top:18px;text-align:center;color:var(--white)"><div class="title-lg">Company <span style="color:var(--night)">Spacegraph</span></div></div>
  <svg class="pad" style="left:30px;top:54px" width="380" height="176" viewBox="0 0 380 176">
    <defs><linearGradient id="areaFill" x1="0" y1="0" x2="0" y2="1"><stop offset="0" stop-color="#0a1f5c" stop-opacity=".9"/><stop offset="1" stop-color="#0a1f5c" stop-opacity=".35"/></linearGradient></defs>
    <g stroke="rgba(255,255,255,.25)" stroke-width=".6">
      <line x1="0" y1="20" x2="380" y2="20"/><line x1="0" y1="55" x2="380" y2="55"/><line x1="0" y1="90" x2="380" y2="90"/><line x1="0" y1="125" x2="380" y2="125"/>
    </g>
    <path d="M0 120 C30 110 50 95 80 100 S130 60 160 70 S200 20 230 40 S280 100 310 80 S350 60 380 90 L380 145 L0 145 Z" fill="url(#areaFill)"/>
    <path d="M0 120 C30 110 50 95 80 100 S130 60 160 70 S200 20 230 40 S280 100 310 80 S350 60 380 90" fill="none" stroke="#ffffff" stroke-width="1.4"/>
    <g fill="#ffffff" font-family="Poppins, sans-serif" font-size="8" text-anchor="middle">
      <text x="30" y="164">Jan</text><text x="94" y="164">Feb</text><text x="158" y="164">Mar</text><text x="222" y="164">Apr</text><text x="286" y="164">May</text><text x="350" y="164">Jun</text>
    </g>
  </svg>
</section>

<section class="slide dark col-right" style="top:1338px" aria-label="Process infographic table">
  <div class="pad" style="left:0;right:0;top:16px;text-align:center"><div class="title-lg">Process Infographic</div></div>
  <div class="pad" style="left:30px;top:50px;width:380px">
    <table>
      <thead><tr>
        <th style="background:var(--night-2)">Task</th>
        <th style="background:var(--blue-deep)">Alpha</th>
        <th style="background:var(--blue-mid)">Beta</th>
        <th style="background:var(--violet)">Gamma</th>
        <th style="background:var(--rose)">Delta</th>
      </tr></thead>
      <tbody>
        <tr><td>Setup</td><td>12</td><td>18</td><td>24</td><td>30</td></tr>
        <tr><td>Review</td><td>15</td><td>22</td><td>19</td><td>27</td></tr>
        <tr><td>Deploy</td><td>20</td><td>14</td><td>31</td><td>25</td></tr>
        <tr><td>Monitor</td><td>11</td><td>26</td><td>17</td><td>33</td></tr>
        <tr><td>Report</td><td>23</td><td>16</td><td>28</td><td>21</td></tr>
      </tbody>
    </table>
  </div>
</section>

<section class="slide col-right" style="top:1610px" aria-label="Our Signal Forge growth">
  <div class="blob" style="left:-60px;top:-60px;width:150px;height:150px;background:var(--mist)"></div>
  <div class="blob grad-sky" style="right:-30px;bottom:-50px;width:130px;height:130px;opacity:.3"></div>
  <div class="pad" style="left:24px;top:46px;width:190px">
    <div class="title-lg accent-blue">Our Signal<br><span class="accent">Forge</span></div>
    <p class="body" style="margin-top:6px">We climb higher with every launch.</p>
    <div style="display:flex;gap:16px;margin-top:12px">
      <svg width="44" height="44" viewBox="0 0 40 40" role="img" aria-label="Growth 72%"><circle cx="20" cy="20" r="16" fill="none" stroke="var(--ice)" stroke-width="4"/><circle cx="20" cy="20" r="16" fill="none" stroke="var(--blue-deep)" stroke-width="4" stroke-dasharray="72 100" pathLength="100" transform="rotate(-90 20 20)"/><text x="20" y="23" text-anchor="middle" font-size="8" font-family="Poppins, sans-serif" fill="var(--blue-deep)">72%</text></svg>
      <svg width="44" height="44" viewBox="0 0 40 40" role="img" aria-label="Uptime 90%"><circle cx="20" cy="20" r="16" fill="none" stroke="var(--ice)" stroke-width="4"/><circle cx="20" cy="20" r="16" fill="none" stroke="var(--teal)" stroke-width="4" stroke-dasharray="90 100" pathLength="100" transform="rotate(-90 20 20)"/><text x="20" y="23" text-anchor="middle" font-size="8" font-family="Poppins, sans-serif" fill="var(--teal)">90%</text></svg>
    </div>
  </div>
  <div class="photo" role="img" aria-label="Cartoon rocket with a round company badge blasting off with a flame trail" style="left:268px;top:30px;width:124px;height:190px;border-radius:62px 62px 24px 24px;background:linear-gradient(170deg,var(--ice),var(--sky) 45%,var(--blue-mid) 75%,var(--violet));z-index:1"></div>
  <span class="page-no">12</span>
</section>

</body>
</html>
```